Boutique Accounting firm needs a sleek, professional facebook page.

We need a facebook page, facebook logo and a template meme/add designed that we can add text to. This page a designs need to tell the client that we are professional, approachable, understand their business needs and that they can be confident that if they work with us they will get an accountant who offers expert advice and service working with them to get the best possible outcome for their business. Our firm is located ina rural area in Gippsland VIC and deals with farmers, tradespeople, small to medium business and individuals.
attached is our logo and we want the grey used and we note that it will need to be resized to ensure it stands out and can be seen clearly.
The final design should promote growth and financial security and understanding.

Examples of pages that we identify with are:
@clearbrookledgersnz
@dunmoreassociatescharteredaccountants
@halvardenterprise

Target Market(s)

small business

Industry/Entity Type

Accounting

Colors
3176b5
0792cd

Requirements
Must have
• our logo must be designed so that the words of our brand fill up the area
Nice to have
• .
Should not have
• .

```html
<!DOCTYPE html>
<html lang="en">
<head>
<meta charset="utf-8">
<title>Hollis Whitford – Facebook Page Kit</title>
<link rel="stylesheet" href="https://fonts.googleapis.com/css2?family=Yanone+Kaffeesatz:wght@400;700&family=Questrial&family=Cinzel:wght@500&display=swap">
<style>
  :root {
    --brand-blue: #3176b5;
    --brand-sky: #33aacc;
    --brand-grey: #7a7a7a;
    --logo-grey: #6f6f6f;
    --paper: #ffffff;
    --ink-dark: #3a3a3a;
    --shadow: 6px 8px 10px rgba(0,0,0,0.35);
  }
  * { margin: 0; padding: 0; box-sizing: border-box; }
  html, body { width: 1200px; height: 3214px; overflow: hidden; background: var(--paper); }
  body { position: relative; font-family: "Yanone Kaffeesatz", "Arial Narrow", sans-serif; }

  .section-title {
    position: absolute; top: 150px; font-weight: 700; font-size: 72px; color: var(--brand-blue);
    text-align: center; line-height: 1; letter-spacing: 1px;
  }
  .section-title.logo-title { left: 60px; width: 280px; }
  .section-title.cover-title { left: 620px; width: 400px; }
  .section-title.post-title { top: 1965px; left: 350px; width: 500px; }

  /* Logo tiles */
  .logo-tile {
    position: absolute; width: 335px; height: 335px; box-shadow: var(--shadow);
    display: flex; flex-direction: column; justify-content: center; padding-left: 26px;
  }
  .logo-tile .wordmark {
    font-family: "Questrial", "Century Gothic", sans-serif; font-size: 74px; line-height: 0.92;
    letter-spacing: -2px;
  }
  .logo-tile .descriptor {
    font-family: "Cinzel", Georgia, serif; font-size: 20px; margin-top: 28px; letter-spacing: 1px;
  }
  .logo-tile.on-blue { left: 28px; top: 279px; background: var(--brand-blue); color: var(--paper); }
  .logo-tile.on-white-sky { left: 37px; top: 654px; background: var(--paper); }
  .logo-tile.on-white-blue { left: 37px; top: 1020px; background: var(--paper); }
  .logo-tile.on-sky { left: 43px; top: 1414px; background: var(--brand-sky); color: var(--paper); }
  .on-white-sky .wordmark { color: var(--brand-sky); }
  .on-white-blue .wordmark { color: var(--brand-blue); }
  .on-white-sky .descriptor, .on-white-blue .descriptor { color: var(--logo-grey); }

  /* Cover art */
  .cover {
    position: absolute; left: 407px; width: 772px; height: 289px; overflow: hidden;
    box-shadow: var(--shadow);
  }
  .cover .panel { position: absolute; top: 0; height: 100%; }
  .cover .panel-left { left: 0; width: 386px; }
  .cover .panel-right { left: 386px; width: 386px; }
  .photo { position: absolute; }
  .cover .photo { left: 258px; top: 11px; width: 272px; height: 270px; }
  .photo-cafe { background: linear-gradient(135deg, #d9c4a4 0%, #8a6a4c 45%, #4a3a30 100%); }
  .photo-family { background: linear-gradient(135deg, #f2f2f2 0%, #d8d4d2 45%, #9a8a86 100%); }

  .bracket { position: absolute; border-color: var(--paper); border-style: solid; border-width: 0; }
  .bracket.bottom-left { border-left-width: 3px; border-bottom-width: 3px; }
  .bracket.top-right { border-top-width: 3px; border-right-width: 3px; }
  .bracket.is-blue { border-color: var(--brand-sky); }

  .cover .bracket.bottom-left { left: 15px; top: 170px; width: 125px; height: 110px; }
  .cover .bracket.top-right { left: 643px; top: 17px; width: 115px; height: 40px; }

  .cover .message { position: absolute; left: 32px; top: 170px; font-size: 25px; line-height: 1.5; color: var(--paper); }
  .cover .message.clients { left: 50px; top: 72px; line-height: 1.45; }
  .cover .tagline { position: absolute; left: 548px; top: 22px; font-size: 32px; line-height: 1.45; color: var(--paper); }
  .cover .phone { position: absolute; left: 548px; top: 180px; font-size: 27px; color: var(--paper); }
  .phone .label { color: var(--brand-sky); }

  .name-lockup { position: absolute; display: flex; flex-direction: column; }
  .name-lockup .name { font-family: "Questrial", "Century Gothic", sans-serif; color: var(--paper); line-height: 1; }
  .name-lockup .descriptor { font-family: "Cinzel", Georgia, serif; color: var(--paper); letter-spacing: 0.5px; }
  .cover .name-lockup { left: 560px; top: 224px; padding: 2px 6px; border-left: 2px solid var(--brand-sky); }
  .cover .name-lockup .name { font-size: 22px; }
  .cover .name-lockup .descriptor { font-size: 8px; }

  .cover.variant-light-right .panel-right { background: var(--paper); }
  .cover.variant-light-right .tagline { color: var(--ink-dark); left: 530px; top: 50px; }
  .cover.variant-light-right .phone { color: var(--brand-blue); left: 530px; top: 155px; }
  .cover.variant-light-right .phone .label { color: var(--brand-blue); }
  .cover.variant-light-right .name-lockup .name { color: var(--brand-blue); }
  .cover.variant-light-right .name-lockup .descriptor { color: var(--brand-blue); }
  .cover.variant-light-right .name-lockup { top: 238px; left: 625px; }
  .cover.variant-light-left .message { color: var(--brand-sky); }

  /* Post template */
  .post { position: absolute; left: 146px; width: 958px; height: 501px; overflow: hidden; box-shadow: var(--shadow); }
  .post .panel { position: absolute; top: 0; height: 100%; }
  .post .panel-left { left: 0; width: 497px; background: var(--brand-sky); }
  .post .panel-right { left: 497px; width: 461px; }
  .post .photo { left: 272px; top: 21px; width: 450px; height: 450px; opacity: 0.92; }
  .post .bracket.bottom-left { left: 14px; top: 290px; width: 240px; height: 195px; }
  .post .bracket.top-right { left: 830px; top: 14px; width: 95px; height: 95px; border-width: 0; border-top-width: 5px; border-right-width: 5px; }
  .post .message { position: absolute; left: 47px; top: 232px; font-size: 44px; line-height: 1.5; color: var(--paper); }
  .post .phone { position: absolute; left: 738px; top: 350px; font-size: 32px; color: var(--paper); }
  .post .name-lockup { left: 738px; top: 408px; padding: 2px 8px; border-left: 3px solid var(--paper); }
  .post .name-lockup .name { font-size: 28px; }
  .post .name-lockup .descriptor { font-size: 10px; }
</style>
</head>
<body>

  <h2 class="section-title logo-title">LOGO</h2>
  <h2 class="section-title cover-title">COVER ART</h2>

  <div class="logo-tile on-blue">
    <div class="wordmark">hollis<br>whitford</div>
    <div class="descriptor">ACCOUNTANTS &amp; ADVISORS</div>
  </div>
  <div class="logo-tile on-white-sky">
    <div class="wordmark">hollis<br>whitford</div>
    <div class="descriptor">ACCOUNTANTS<br>&amp; ADVISORS</div>
  </div>
  <div class="logo-tile on-white-blue">
    <div class="wordmark">hollis<br>whitford</div>
    <div class="descriptor">ACCOUNTANTS<br>&amp; ADVISORS</div>
  </div>
  <div class="logo-tile on-sky">
    <div class="wordmark">hollis<br>whitford</div>
    <div class="descriptor">ACCOUNTANTS &amp; ADVISORS</div>
  </div>

  <!-- Cover 1 -->
  <div class="cover" style="top:279px">
    <div class="panel panel-left" style="background:var(--brand-sky)"></div>
    <div class="panel panel-right" style="background:var(--brand-grey)"></div>
    <div class="photo photo-cafe" role="img" aria-label="Photo of two small business owners in a café looking at a tablet together"></div>
    <div class="bracket bottom-left"></div>
    <div class="bracket top-right is-blue"></div>
    <p class="message">Embracing Change.<br>"We are at one with Technology"</p>
    <p class="tagline">"An Instinct for<br>Financial Success."</p>
    <p class="phone"><span class="label">Ph.</span> 03 5550 0142</p>
    <div class="name-lockup"><span class="name">hollis whitford</span><span class="descriptor">ACCOUNTANTS &amp; ADVISORS</span></div>
  </div>

  <!-- Cover 2 -->
  <div class="cover" style="top:606px">
    <div class="panel panel-left" style="background:var(--brand-blue)"></div>
    <div class="panel panel-right" style="background:var(--brand-grey)"></div>
    <div class="photo photo-cafe" role="img" aria-label="Photo of two small business owners in a café looking at a tablet together"></div>
    <div class="bracket bottom-left"></div>
    <div class="bracket top-right is-blue"></div>
    <p class="message">Embracing Change.<br>"We are at one with Technology"</p>
    <p class="tagline">"An Instinct for<br>Financial Success."</p>
    <p class="phone"><span class="label">Ph.</span> 03 5550 0142</p>
    <div class="name-lockup"><span class="name">hollis whitford</span><span class="descriptor">ACCOUNTANTS &amp; ADVISORS</span></div>
  </div>

  <!-- Cover 3 -->
  <div class="cover variant-light-right" style="top:928px">
    <div class="panel panel-left" style="background:var(--brand-blue)"></div>
    <div class="panel panel-right"></div>
    <div class="photo photo-family" role="img" aria-label="Photo of an advisor meeting a family with children on a sofa"></div>
    <div class="bracket bottom-left" style="left:22px;top:200px;width:60px;height:70px"></div>
    <div class="bracket top-right is-blue"></div>
    <p class="message clients">Our Clients Are<br>"Aspirational and value<br>quality advice and relationships."</p>
    <p class="tagline">"An Instinct for<br>Financial Success."</p>
    <p class="phone"><span class="label">Ph.</span> 03 5550 0142</p>
    <div class="name-lockup"><span class="name">hollis whitford</span><span class="descriptor">ACCOUNTANTS &amp; ADVISORS</span></div>
  </div>

  <!-- Cover 4 -->
  <div class="cover" style="top:1260px">
    <div class="panel panel-left" style="background:var(--brand-sky)"></div>
    <div class="panel panel-right" style="background:var(--brand-grey)"></div>
    <div class="photo photo-family" role="img" aria-label="Photo of an advisor meeting a family with children on a sofa"></div>
    <div class="bracket bottom-left"></div>
    <div class="bracket top-right is-blue"></div>
    <p class="message clients" style="left:35px">Our Clients Are<br>"Aspirational and value<br>quality advice and relationships."</p>
    <p class="tagline">"An Instinct for<br>Financial Success."</p>
    <p class="phone"><span class="label">Ph.</span> 03 5550 0142</p>
    <div class="name-lockup"><span class="name">hollis whitford</span><span class="descriptor">ACCOUNTANTS &amp; ADVISORS</span></div>
  </div>

  <!-- Cover 5 -->
  <div class="cover variant-light-left" style="top:1596px">
    <div class="panel panel-left" style="background:var(--paper)"></div>
    <div class="panel panel-right" style="background:var(--brand-grey)"></div>
    <div class="photo photo-family" role="img" aria-label="Photo of an advisor meeting a family with children on a sofa"></div>
    <div class="bracket bottom-left is-blue"></div>
    <div class="bracket top-right is-blue"></div>
    <p class="message clients" style="left:35px;top:150px">Our Clients Are<br>"Aspirational and value<br>quality advice and relationships."</p>
    <p class="tagline">"An Instinct for<br>Financial Success."</p>
    <p class="phone"><span class="label">Ph.</span> 03 5550 0142</p>
    <div class="name-lockup"><span class="name">hollis whitford</span><span class="descriptor">ACCOUNTANTS &amp; ADVISORS</span></div>
  </div>

  <h2 class="section-title post-title">POST MEME</h2>

  <!-- Post template, blue -->
  <div class="post" style="top:2070px">
    <div class="panel panel-left"></div>
    <div class="panel panel-right" style="background:var(--brand-blue)"></div>
    <div class="photo photo-cafe" role="img" aria-label="Photo of two small business owners in a café looking at a tablet together"></div>
    <div class="bracket bottom-left"></div>
    <div class="bracket top-right"></div>
    <p class="message">Embracing Change.<br>"We are at one with Technology"</p>
    <p class="phone">Ph. 03 5550 0142</p>
    <div class="name-lockup"><span class="name">hollis whitford</span><span class="descriptor">ACCOUNTANTS &amp; ADVISORS</span></div>
  </div>

  <!-- Post template, grey -->
  <div class="post" style="top:2625px">
    <div class="panel panel-left"></div>
    <div class="panel panel-right" style="background:var(--brand-grey)"></div>
    <div class="photo photo-cafe" role="img" aria-label="Photo of two small business owners in a café looking at a tablet together"></div>
    <div class="bracket bottom-left"></div>
    <div class="bracket top-right is-blue"></div>
    <p class="message">Embracing Change.<br>"We are at one with Technology"</p>
    <p class="phone"><span class="label">Ph.</span> 03 5550 0142</p>
    <div class="name-lockup" style="border-left-color:var(--brand-sky)"><span class="name">hollis whitford</span><span class="descriptor">ACCOUNTANTS &amp; ADVISORS</span></div>
  </div>

</body>
</html>
```